I need a simple, classy and stylish business card. I would like it to have a black background with white writing. I would like you to use my logo you designed on the front with the word 'Imagery" used underneath it in the same font. On the back I was thinking of the website at the top 'tomverrick.com' Then my social media accounts, Can you use the instagram, Facebook and twitter logo then my handles?
Please let me know what you think.
Regards Tom
Must have
- Website: www.tomverrick.com
- Social media handles..
- Instagram: @Tom_Verrick_Imagery
- Facebook: Tom Verrick Imagery
- Twitter: @Tom_Verrick
- Email: info@tomverick.com
- Phone: 0437 518 293

```html
<!DOCTYPE html>
<html lang="en">
<head>
<meta charset="utf-8">
<title>Tom Verrick Imagery – Business Card</title>
<link rel="stylesheet" href="https://fonts.googleapis.com/css2?family=Open+Sans:wght@300;400&family=Roboto+Condensed:wght@700&display=swap">
<style>
  :root {
    --backdrop: #e9e6e1;
    --card-black: #050505;
    --card-white: #ffffff;
    --ink-white: #ffffff;
    --card-shadow: rgba(0, 0, 0, 0.28);
  }
  * { margin: 0; padding: 0; box-sizing: border-box; }
  html, body {
    width: 1200px;
    height: 900px;
    overflow: hidden;
    background: var(--backdrop);
  }
  .canvas {
    position: relative;
    width: 1200px;
    height: 900px;
  }
  .card {
    position: absolute;
    left: 290px;
    width: 620px;
    height: 354px;
    background: var(--card-black);
    box-shadow: 0 10px 24px var(--card-shadow);
    overflow: hidden;
    color: var(--ink-white);
  }
  .card--back { top: 64px; }
  .card--front { top: 482px; }

  /* Back: contact block on the right half */
  .contact {
    position: absolute;
    left: 350px;
    top: 104px;
    list-style: none;
  }
  .contact__item {
    display: flex;
    align-items: center;
    gap: 10px;
    font-family: "Open Sans", sans-serif;
    font-weight: 400;
    font-size: 14px;
    line-height: 25px;
    color: var(--ink-white);
    white-space: nowrap;
  }
  .contact__marker {
    width: 13px;
    height: 13px;
    background: var(--ink-white);
    flex: none;
  }
  .contact__web {
    position: absolute;
    left: 350px;
    top: 244px;
    font-family: "Roboto Condensed", sans-serif;
    font-weight: 700;
    font-size: 23px;
    color: var(--ink-white);
    white-space: nowrap;
  }

  /* Front: name lockup + white footer band */
  .front-brand {
    position: absolute;
    left: 150px;
    top: 110px;
    display: flex;
    align-items: center;
    gap: 22px;
  }
  .brand-dot {
    width: 30px;
    height: 30px;
    border-radius: 50%;
    background: var(--ink-white);
    flex: none;
  }
  .brand-name {
    font-family: "Open Sans", sans-serif;
    font-weight: 300;
    color: var(--ink-white);
    white-space: nowrap;
  }
  .brand-name__main {
    display: block;
    font-size: 40px;
    line-height: 1.1;
  }
  .brand-name__sub {
    display: block;
    font-size: 26px;
    line-height: 1.1;
    padding-left: 36px;
  }
  .front-band {
    position: absolute;
    left: 0;
    bottom: 0;
    width: 620px;
    height: 44px;
  }
</style>
</head>
<body>
<main class="canvas">

  <section class="card card--back" aria-label="Business card back">
    <ul class="contact">
      <li class="contact__item"><span class="contact__marker"></span>@Tom_Verrick_Imagery</li>
      <li class="contact__item"><span class="contact__marker"></span>@TomVerrickImagery</li>
      <li class="contact__item"><span class="contact__marker"></span>@Tom_Verrick</li>
      <li class="contact__item"><span class="contact__marker"></span>info@tomverick.com</li>
      <li class="contact__item"><span class="contact__marker"></span>0437 518 293</li>
    </ul>
    <p class="contact__web">www.tomverrick.com</p>
  </section>

  <section class="card card--front" aria-label="Business card front">
    <div class="front-brand">
      <span class="brand-dot"></span>
      <p class="brand-name">
        <span class="brand-name__main">Tom Verrick</span>
        <span class="brand-name__sub">Imagery</span>
      </p>
    </div>
    <svg class="front-band" viewBox="0 0 620 44" aria-hidden="true">
      <rect x="0" y="0" width="620" height="44" fill="var(--card-white)"/>
      <polygon points="262,0 276,0 270,44 256,44" fill="var(--card-black)"/>
    </svg>
  </section>

</main>
</body>
</html>
```